Banner Ad Design Project

I need banners made for the following site: http://www.velmorquistanbo.com

Sizes needed are:

728x90
200x200
160x600
120x600
300x250
336x280

Info:

You do not have to theme it around the colors used on the website. You can create your own colors if you want.

Taglines that you can use are:

"Learn how to receive hundreds of messages from women in less than an hour using a new software tool"

"Hack online dating websites and bombard your inbox with eager women wanting to learn more about you"

"Boost your dating site profile views by 486%"

"BANNED! Find out why this software tool that messages hundreds of women in minutes was banned by the online dating websites. Click Here"

I am looking for good calls to action, spark curiosity, and a clickable ad. Please ask any and all questions.

Target Market(s)

Single Men 18-45

Industry/Entity Type

Software

Requirements
Must have
• - Call to action (i.e. Click Here, Download Now, etc)
- Clear easy to read font, colors, and design.
- Must be 50kb or smaller to use on bidplume. If you have design that is over submit draft and I might make exception.

```html
<!DOCTYPE html>
<html lang="en">
<head>
<meta charset="utf-8">
<title>Velmorquistanbo – Skyscraper Banner Sequence</title>
<link rel="stylesheet" href="https://fonts.googleapis.com/css2?family=Anton&family=Open+Sans:wght@400;600&display=swap">
<style>
  :root {
    --page-bg: #e9e4df;
    --panel-dark: #231f20;
    --panel-dark-2: #3a3637;
    --message-bg: #ffffff;
    --ink: #1d1b1b;
    --accent-red: #e0252b;
    --button-top: #5aa8e8;
    --button-bottom: #1f6fc4;
    --light-text: #ffffff;
  }
  * { box-sizing: border-box; margin: 0; padding: 0; }
  html, body { width: 1200px; height: 900px; overflow: hidden; }
  body {
    background: var(--page-bg);
    font-family: "Open Sans", sans-serif;
  }
  .sequence {
    position: absolute;
    top: 115px;
    left: 93px;
    display: flex;
    gap: 30px;
  }
  .banner {
    position: relative;
    width: 180px;
    height: 674px;
    background: var(--panel-dark);
    overflow: hidden;
  }
  .banner__bubble {
    position: absolute;
    top: 0; left: 0;
    width: 180px; height: 390px;
  }
  .banner__message {
    position: absolute;
    top: 0; left: 0; right: 0;
    height: 345px;
    text-align: center;
    font-family: "Anton", sans-serif;
    color: var(--ink);
  }
  .headline {
    position: absolute;
    left: 0; right: 0;
    font-size: 39px;
    line-height: 45px;
    letter-spacing: 0.5px;
  }
  .headline--boost { top: 132px; font-size: 58px; line-height: 70px; color: var(--accent-red); }
  .headline--stack { top: 100px; }
  .headline--stat { top: 136px; font-size: 62px; line-height: 74px; color: var(--accent-red); letter-spacing: 0; }
  .headline .is-red { color: var(--accent-red); }
  .cta-button {
    position: absolute;
    left: 12px;
    top: 299px;
    width: 156px;
    height: 40px;
    border-radius: 20px;
    background: linear-gradient(var(--button-top), var(--button-bottom));
    color: var(--light-text);
    font-family: "Open Sans", sans-serif;
    font-size: 19px;
    line-height: 40px;
    text-align: center;
    padding-left: 14px;
  }
  .cta-button::before {
    content: "";
    position: absolute;
    left: 12px; top: 16px;
    border-left: 5px solid var(--light-text);
    border-top: 4px solid transparent;
    border-bottom: 4px solid transparent;
  }
  .banner__illustration {
    position: absolute;
    left: 0; right: 0;
    top: 395px;
    height: 200px;
    background: radial-gradient(ellipse at 50% 70%, #4a4647 0%, var(--panel-dark-2) 35%, var(--panel-dark) 75%);
  }
  .brand {
    position: absolute;
    left: 0; right: 0;
    top: 610px;
    display: flex;
    align-items: center;
    justify-content: center;
    gap: 7px;
  }
  .brand__mark {
    width: 14px; height: 14px;
    border-radius: 50%;
    background: var(--accent-red);
  }
  .brand__name {
    font-family: "Open Sans", sans-serif;
    font-weight: 600;
    font-size: 17px;
    color: var(--light-text);
  }
  .brand__tagline {
    position: absolute;
    left: 0; right: 0;
    top: 636px;
    text-align: center;
    font-size: 9px;
    color: var(--light-text);
  }
</style>
</head>
<body>
<main class="sequence">

  <section class="banner">
    <svg class="banner__bubble" viewBox="0 0 180 390" aria-hidden="true"><path d="M0,0 H180 V347 Q150,366 102,369 L90,386 L78,369 Q30,366 0,347 Z" fill="var(--message-bg)"/></svg>
    <div class="banner__message"><p class="headline headline--boost">BOOST</p></div>
    <div class="banner__illustration" role="img" aria-label="White silhouette of a man with a red heart, surrounded by an arc of small women figures on radiating dark rays"></div>
    <div class="brand"><span class="brand__mark"></span><span class="brand__name">Velmorquistanbo</span></div>
    <p class="brand__tagline">Elevate Your Matches</p>
  </section>

  <section class="banner">
    <svg class="banner__bubble" viewBox="0 0 180 390" aria-hidden="true"><path d="M0,0 H180 V347 Q150,366 102,369 L90,386 L78,369 Q30,366 0,347 Z" fill="var(--message-bg)"/></svg>
    <div class="banner__message"><p class="headline headline--stack">YOUR<br>DATING<br>SITE</p></div>
    <div class="banner__illustration" role="img" aria-label="White silhouette of a man with a red heart, surrounded by an arc of small women figures on radiating dark rays"></div>
    <div class="brand"><span class="brand__mark"></span><span class="brand__name">Velmorquistanbo</span></div>
    <p class="brand__tagline">Elevate Your Matches</p>
  </section>

  <section class="banner">
    <svg class="banner__bubble" viewBox="0 0 180 390" aria-hidden="true"><path d="M0,0 H180 V347 Q150,366 102,369 L90,386 L78,369 Q30,366 0,347 Z" fill="var(--message-bg)"/></svg>
    <div class="banner__message"><p class="headline headline--stack">YOUR<br>DATING<br>SITE<br><span class="is-red">PROFILE<br>by</span></p></div>
    <div class="banner__illustration" role="img" aria-label="White silhouette of a man with a red heart, surrounded by an arc of small women figures on radiating dark rays"></div>
    <div class="brand"><span class="brand__mark"></span><span class="brand__name">Velmorquistanbo</span></div>
    <p class="brand__tagline">Elevate Your Matches</p>
  </section>

  <section class="banner">
    <svg class="banner__bubble" viewBox="0 0 180 390" aria-hidden="true"><path d="M0,0 H180 V347 Q150,366 102,369 L90,386 L78,369 Q30,366 0,347 Z" fill="var(--message-bg)"/></svg>
    <div class="banner__message"><p class="headline headline--stat">486%</p></div>
    <div class="banner__illustration" role="img" aria-label="White silhouette of a man with a red heart, surrounded by an arc of small women figures on radiating dark rays"></div>
    <div class="brand"><span class="brand__mark"></span><span class="brand__name">Velmorquistanbo</span></div>
    <p class="brand__tagline">Elevate Your Matches</p>
  </section>

  <section class="banner">
    <svg class="banner__bubble" viewBox="0 0 180 390" aria-hidden="true"><path d="M0,0 H180 V347 Q150,366 102,369 L90,386 L78,369 Q30,366 0,347 Z" fill="var(--message-bg)"/></svg>
    <div class="banner__message">
      <p class="headline headline--stat">486%</p>
      <a class="cta-button">Learn How</a>
    </div>
    <div class="banner__illustration" role="img" aria-label="White silhouette of a man with a red heart, surrounded by small women figures, one with a red heart above her"></div>
    <div class="brand"><span class="brand__mark"></span><span class="brand__name">Velmorquistanbo</span></div>
    <p class="brand__tagline">Elevate Your Matches</p>
  </section>

</main>
</body>
</html>
```